New boutique IT consultancy needs business card

I need a business card and logo for my IT consultancy business, called 'Quenmarlo' . I want it to make me look bigger than I am. I want it to look classy, and modern. Simple design, that will be easy for me to translate into my webpage etc. The business card should be bold, and different.

The logo should emphasise the 'y' as used in quenmarlo

Target Market(s)

IT divisions in other companies

Industry/Entity Type

Business

Contact Information for Business Card

Doreen Pakfield
Director
+61 437 918 205
dpakfield@quenmarlo-mail.test

```html
<!DOCTYPE html>
<html lang="en">
<head>
<meta charset="utf-8">
<title>Quenmarlo — Business Card</title>
<link rel="stylesheet" href="https://fonts.googleapis.com/css2?family=Roboto:wght@400;500;700&display=swap">
<style>
  :root {
    --backdrop: #2b2b2d;
    --card: #363638;
    --card-edge: #3d3d40;
    --ink: #f2f2f2;
    --ink-soft: #d9d9d9;
    --ink-muted: #a9a9ad;
    --lime: #b5d334;
    --icon: #e0e21c;
    --faint: rgba(255,255,255,0.06);
  }
  * { margin: 0; padding: 0; box-sizing: border-box; }
  html, body {
    width: 900px; height: 1200px; overflow: hidden;
    background: var(--backdrop);
    font-family: "Roboto", Arial, sans-serif;
  }
  .sheet {
    width: 900px; height: 1200px;
    display: flex; flex-direction: column;
    justify-content: space-around; align-items: center;
  }
  .card {
    position: relative;
    width: 560px; height: 320px;
    background: var(--card);
    border: 1px solid var(--card-edge);
    border-radius: 3px;
    box-shadow: 0 18px 40px rgba(0,0,0,0.45);
    overflow: hidden;
  }
  .brand {
    position: absolute; left: 0; right: 0;
    text-align: center;
  }
  .brand__name {
    display: block;
    font-weight: 700; font-size: 30px;
    letter-spacing: 2px; color: var(--ink);
    text-transform: uppercase;
    line-height: 1.1;
  }
  .brand__tagline {
    display: block; margin-top: 6px;
    font-size: 11px; font-weight: 400;
    letter-spacing: 1px;
    color: var(--ink-muted);
  }
  .card--front .backdrop-disc {
    position: absolute; left: 50%; top: 50%;
    width: 250px; height: 250px; margin: -125px 0 0 -125px;
    border-radius: 50%; background: var(--faint);
  }
  .card--front .brand { top: 130px; }
  .card--back .brand-disc {
    position: absolute; left: 50%; top: 40px;
    width: 62px; height: 62px; margin-left: -31px;
    border-radius: 50%;
    background: var(--lime);
  }
  .card--back .brand { top: 118px; }
  .holder {
    position: absolute; left: 36px; bottom: 34px;
    color: var(--ink); font-size: 13px; line-height: 1.4;
  }
  .holder__name { font-weight: 500; font-size: 15px; letter-spacing: 0.5px; text-transform: uppercase; }
  .holder__role { color: var(--icon); font-weight: 500; }
  .contacts {
    position: absolute; right: 36px; top: 200px;
    list-style: none; color: var(--ink-soft); font-size: 12.5px; line-height: 1.5;
  }
  .contacts li { display: flex; align-items: center; gap: 7px; white-space: nowrap; }
  .contacts svg { width: 11px; height: 11px; flex: none; }
</style>
</head>
<body>
<main class="sheet">
  <section class="card card--front" aria-label="Card front">
    <div class="backdrop-disc"></div>
    <div class="brand">
      <span class="brand__name">Quenmarlo</span>
      <span class="brand__tagline">Clear systems, calm teams</span>
    </div>
  </section>

  <section class="card card--back" aria-label="Card back">
    <div class="brand-disc"></div>
    <div class="brand">
      <span class="brand__name">Quenmarlo</span>
      <span class="brand__tagline">Clear systems, calm teams</span>
    </div>

    <div class="holder">
      <div class="holder__name">Doreen Pakfield</div>
      <div class="holder__role">Director</div>
      <div>48 Harbour Lane, Suite 12</div>
      <div>City, State, Zip Code</div>
    </div>

    <ul class="contacts">
      <li><svg viewBox="0 0 11 11"><rect width="11" height="11" fill="#e0e21c"/><path d="M3 2.5l1.3 0 .6 1.6-.8.6a4.5 4.5 0 0 0 2.2 2.2l.6-.8 1.6.6v1.3c-3 .2-5.7-2.5-5.5-5.5z" fill="#363638"/></svg>+61 437 918 205</li>
      <li><svg viewBox="0 0 11 11"><rect width="11" height="11" fill="#e0e21c"/><path d="M3 2.5l1.3 0 .6 1.6-.8.6a4.5 4.5 0 0 0 2.2 2.2l.6-.8 1.6.6v1.3c-3 .2-5.7-2.5-5.5-5.5z" fill="#363638"/></svg>+45 286 410 973</li>
      <li><svg viewBox="0 0 11 11"><rect width="11" height="11" fill="#e0e21c"/><rect x="2" y="3" width="7" height="5" fill="none" stroke="#363638" stroke-width="1"/><path d="M2 3l3.5 3L9 3" fill="none" stroke="#363638" stroke-width="1"/></svg>dpakfield@quenmarlo-mail.test</li>
      <li><svg viewBox="0 0 11 11"><rect width="11" height="11" fill="#e0e21c"/><circle cx="5.5" cy="5.5" r="3" fill="none" stroke="#363638" stroke-width="1"/><path d="M2.5 5.5h6M5.5 2.5v6" stroke="#363638" stroke-width="0.8"/></svg>www.quenmarlo-web.test</li>
    </ul>
  </section>
</main>
</body>
</html>
```